creating a certificate for our flagship course

Hi,
We need a new certificate for our flagship course called Bright Harbour. We have been running this course for 25 years this year and want to get something special that represents that. We need our logos incorporated and we love to have a compass or Koru incorporated in the certificate. We like something different from your standard certificate, but not too crazy.

The text should say something along the lines of:
This certificate is awarded to ....
For successfully completing and contributing to the three day Bright Harbour programme.

signed:... date:...

to learn a bit more about this course and our company, please check our website. www.hollisvantreeve.co.nz

Thank you!

Target Market(s)

attendees who completed our 3 day programme.

Requirements
Must have
• Both our BH logo and our brand logo. a compass or a koru.
• a 25th year existence something on it.

```html
<!DOCTYPE html>
<html lang="en">
<head>
<meta charset="utf-8">
<title>Bright Harbour Certificate</title>
<link rel="stylesheet" href="https://fonts.googleapis.com/css2?family=Cinzel:wght@400;500;700&family=Tinos:ital,wght@0,400;0,700;1,400&family=Roboto:wght@400&display=swap">
<style>
  :root {
    --backdrop: #b4b4b8;
    --gold: #c9a673;
    --gold-light: #dcc08f;
    --gold-dark: #a98656;
    --navy: #2a2540;
    --ink: #1f1b33;
    --paper: #ffffff;
    --paper-tone: #eef0ef;
    --green: #8cc63f;
    --muted: #555566;
    --grey-text: #8a8a94;
  }
  html, body {
    margin: 0;
    width: 1200px;
    height: 1200px;
    overflow: hidden;
    background: var(--backdrop);
  }
  .certificate {
    position: absolute;
    left: 197px;
    top: 50px;
    width: 806px;
    height: 1100px;
    background: var(--gold);
    box-shadow: 0 6px 24px rgba(0,0,0,0.25);
  }
  .side-panel {
    position: absolute;
    left: 18px;
    top: 16px;
    width: 261px;
    height: 1068px;
    background: var(--navy);
    overflow: hidden;
  }
  .anniversary-badge {
    position: absolute;
    left: 25px;
    top: 135px;
    width: 210px;
    height: 210px;
    border-radius: 50%;
    background: radial-gradient(circle, var(--gold-light) 0%, var(--gold) 62%, var(--gold-dark) 100%);
    box-shadow: inset 0 0 0 6px var(--gold-dark), inset 0 0 0 10px var(--gold-light);
    display: flex;
    flex-direction: column;
    align-items: center;
    justify-content: center;
    color: var(--navy);
    font-family: "Cinzel", serif;
  }
  .anniversary-badge .years {
    font-size: 72px;
    font-weight: 700;
    line-height: 72px;
  }
  .anniversary-badge .years sup {
    font-size: 28px;
    vertical-align: 30px;
  }
  .anniversary-badge .label {
    font-size: 26px;
    font-weight: 700;
    letter-spacing: 4px;
    line-height: 30px;
  }
  .programme-mark {
    position: absolute;
    left: 32px;
    top: 947px;
    display: flex;
    align-items: center;
    gap: 12px;
    color: var(--paper);
    font: 400 20px "Roboto", sans-serif;
  }
  .programme-mark .square {
    width: 52px;
    height: 52px;
    background: var(--green);
  }
  .main-panel {
    position: absolute;
    left: 279px;
    top: 16px;
    width: 509px;
    height: 1068px;
    background: linear-gradient(160deg, var(--paper) 0%, var(--paper-tone) 100%);
  }
  .brand {
    position: absolute;
    left: 46px;
    top: 71px;
    display: flex;
    align-items: center;
    gap: 22px;
    color: var(--ink);
    font-family: "Cinzel", serif;
    font-weight: 400;
  }
  .brand .square {
    width: 86px;
    height: 86px;
    background: var(--navy);
  }
  .brand .name {
    font-size: 33px;
    line-height: 36px;
    letter-spacing: 2px;
  }
  .brand .name small {
    font-family: "Tinos", serif;
    font-size: 18px;
    letter-spacing: 0;
    color: var(--grey-text);
  }
  .intro {
    position: absolute;
    left: 38px;
    top: 316px;
    margin: 0;
    color: var(--ink);
    font: 400 19px "Cinzel", serif;
    letter-spacing: 1px;
  }
  .awarded {
    position: absolute;
    left: 36px;
    top: 356px;
    margin: 0;
    color: var(--ink);
    font: 400 48px "Cinzel", serif;
    letter-spacing: 2px;
  }
  .name-line {
    position: absolute;
    left: 27px;
    width: 455px;
    border-top: 5px dotted var(--ink);
  }
  .name-line.first { top: 508px; }
  .name-line.second { top: 606px; }
  .citation {
    position: absolute;
    left: 25px;
    top: 655px;
    width: 420px;
    margin: 0;
    color: var(--ink);
    font: italic 400 24px/31px "Tinos", serif;
  }
  .citation strong {
    font-style: normal;
    font-weight: 700;
  }
  .sign-off {
    position: absolute;
    left: 27px;
    top: 1018px;
    display: flex;
    gap: 36px;
    color: var(--muted);
    font: italic 400 12px "Tinos", serif;
  }
  .sign-off span {
    display: inline-block;
    border-bottom: 1px dotted var(--muted);
    padding-right: 4px;
  }
  .sign-off .signed { width: 226px; }
  .sign-off .date { width: 104px; }
</style>
</head>
<body>
  <main class="certificate">
    <aside class="side-panel" role="img" aria-label="Deep navy panel with a tonal koru swirl pattern">
      <div class="anniversary-badge" role="img" aria-label="Gold compass emblem celebrating the 25th year">
        <span class="years">25<sup>th</sup></span>
        <span class="label">YEAR</span>
      </div>
      <div class="programme-mark">
        <div class="square"></div>
        <span>Bright Harbour</span>
      </div>
    </aside>
    <section class="main-panel" role="img" aria-label="White panel with a faint grey koru swirl pattern">
      <div class="brand">
        <div class="square"></div>
        <div class="name">HOLLIS<br>VANTREEVE <small>&amp; Associates</small></div>
      </div>
      <p class="intro">This certificate is</p>
      <h1 class="awarded">AWARDED TO ....</h1>
      <div class="name-line first"></div>
      <div class="name-line second"></div>
      <p class="citation">For successfully completing and contributing to the <strong>three day Bright Harbour</strong> programme.</p>
      <div class="sign-off">
        <span class="signed">Signed:</span>
        <span class="date">Date:</span>
      </div>
    </section>
  </main>
</body>
</html>
```